Talvero Networks LLC
Consultant, Health Care Operations
Talvero Networks LLC -
Creative Brief
Use specific fonts
I like Calibri, Tahoma, Lucida (rounded but professional) but am open to other similar fonts
Simple
Dwight Pennock
President, CEO
PO BOX 418263 Maple Hollow, FL 34912
dwight@talverohub.com
talverohub.com

```html
<!DOCTYPE html>
<html lang="en">
<head>
<meta charset="utf-8">
<title>Talvero Networks LLC – Business Card</title>
<link rel="stylesheet" href="https://fonts.googleapis.com/css2?family=Open+Sans:wght@400;600;700;800&display=swap">
<style>
  :root {
    --page-bg: #efeae2;
    --card-white: #ffffff;
    --brand-blue: #1b93e4;
    --brand-blue-deep: #0b6cc2;
    --wave-black: #111418;
    --brand-navy: #1f2b45;
    --text-light: #ffffff;
    --text-soft: #dcefff;
  }
  * { margin: 0; padding: 0; box-sizing: border-box; }
  html, body {
    width: 1200px; height: 935px; overflow: hidden;
    background: var(--page-bg);
    font-family: "Open Sans", Tahoma, sans-serif;
  }
  .business-card {
    position: absolute; left: 80px; top: 170px;
    width: 1040px; height: 594px;
    border-radius: 46px; overflow: hidden;
    background: var(--card-white);
    box-shadow: 0 10px 30px rgba(0,0,0,0.18);
  }
  .card-waves { position: absolute; inset: 0; width: 100%; height: 100%; }
  .brand-lockup {
    position: absolute; left: 590px; top: 240px;
    display: flex; align-items: center; gap: 16px;
  }
  .brand-dot {
    width: 44px; height: 44px; border-radius: 50%;
    background: var(--brand-blue);
  }
  .brand-name {
    font-size: 68px; font-weight: 800; letter-spacing: 1px;
    color: var(--brand-navy); line-height: 1;
  }
  .holder {
    position: absolute; right: 590px; top: 452px;
    text-align: right; color: var(--text-light);
  }
  .holder-name { font-size: 34px; font-weight: 700; line-height: 1.2; }
  .holder-title { font-size: 20px; font-weight: 400; color: var(--text-soft); margin-top: 4px; }
  .contact-list {
    position: absolute; left: 590px; top: 404px;
    list-style: none; color: var(--text-light);
    font-size: 25px; line-height: 1.38;
  }
</style>
</head>
<body>
  <article class="business-card">
    <svg class="card-waves" viewBox="0 0 1040 594" preserveAspectRatio="none" aria-hidden="true">
      <defs>
        <linearGradient id="bandBlue" x1="0" y1="0" x2="1" y2="1">
          <stop offset="0" stop-color="#2aa2ec"/>
          <stop offset="1" stop-color="#0b6cc2"/>
        </linearGradient>
      </defs>
      <path d="M0 330 C 260 280, 520 420, 1040 318 L1040 338 C 560 420, 300 330, 0 372 Z" fill="var(--wave-black)"/>
      <path d="M0 372 C 300 330, 560 420, 1040 338 L1040 350 C 560 432, 300 344, 0 384 Z" fill="#e9f3fb"/>
      <path d="M0 384 C 300 344, 560 432, 1040 350 L1040 594 L0 594 Z" fill="url(#bandBlue)"/>
    </svg>

    <div class="brand-lockup">
      <span class="brand-dot"></span>
      <span class="brand-name">Talvero</span>
    </div>

    <div class="holder">
      <p class="holder-name">Dwight Pennock</p>
      <p class="holder-title">President, CEO</p>
    </div>

    <ul class="contact-list">
      <li>PO BOX 418263</li>
      <li>Maple Hollow, FL 34912</li>
      <li>Phone : 347.555.0182</li>
      <li>Email : dwight@talverohub.com</li>
      <li>Web : talverohub.com</li>
    </ul>
  </article>
</body>
</html>
```